Handmade Soap Packaging Box Design

Product die line box design for 6 soaps. Box can be any size you want with references provided in the files attached. Minimalistic and luxury is the style. Elements can be taken from the incense .ai files to keep the branding on point.
Our soaps are made from raw materials, ingredients and natural extracts, it’s not irritating to the skin, also still the value and qualifications obtained from nature. The quality and aroma are unique. No ingredients that have SLS & SLES, without TRIETHANOLAMINE, chemical added bubble, bleach and any hazardous chemicals so it can be used on all skin types, even sensitive skin. Hand made, not test on animals, vegan friendly, Non GMO, 99.99% Natural. Made in Thailand

Target Market(s)

Luxury- It is for 6 pieces of Soap packaging. Not 1 soap box

Industry/Entity Type

Health and Beauty

Font styles to use
Serif
Sans Serif
Decorative
Script

Requirements
Must have
• Morvel branding and follow guidelines of the style guide.
Nice to have
• cardboard soap wrapping around each soap bar
Should not have
• cheap stock images.

```html
<!DOCTYPE html>
<html lang="en">
<head>
<meta charset="utf-8">
<title>Morvel – Scent Labels</title>
<link rel="stylesheet" href="https://fonts.googleapis.com/css2?family=Cinzel:wght@400;700&family=Raleway:wght@400;700&display=swap">
<style>
  :root {
    --paper: #ffffff;
    --label-bg: #070505;
    --gold: #c9a449;
    --gold-light: #e8cf7e;
    --red: #d4212a;
    --white: #f2f2f2;
    --green: #23b04a;
    --purple: #6a2c91;
    --cream: #e8e0ad;
    --orange: #d9822e;
  }
  * { box-sizing: border-box; margin: 0; padding: 0; }
  html, body { width: 894px; height: 1200px; overflow: hidden; background: var(--paper); }
  .sheet { position: relative; width: 894px; height: 1200px; }

  .label {
    position: absolute; width: 247px; height: 539px;
    background: var(--label-bg); overflow: hidden;
  }
  .label--dragon   { left: 54px;  top: 49px;  --accent: var(--red); }
  .label--sage     { left: 328px; top: 49px;  --accent: var(--white); }
  .label--rain     { left: 594px; top: 49px;  --accent: var(--green); }
  .label--lavender { left: 64px;  top: 620px; --accent: var(--purple); }
  .label--patch    { left: 332px; top: 620px; --accent: var(--cream); }
  .label--frank    { left: 592px; top: 620px; --accent: var(--orange); }

  /* Mandala ornament areas: flat toned placeholders in the accent colour */
  .mandala { position: absolute; }
  .mandala--top {
    left: 22px; top: 40px; width: 203px; height: 130px;
    border-radius: 50% 50% 8% 8% / 85% 85% 10% 10%;
    background: linear-gradient(180deg,
      color-mix(in srgb, var(--accent) 55%, var(--label-bg)) 0%,
      color-mix(in srgb, var(--accent) 35%, var(--label-bg)) 70%,
      color-mix(in srgb, var(--accent) 12%, var(--label-bg)) 100%);
  }
  .mandala--top-wing {
    left: 0; top: 150px; width: 247px; height: 30px;
    border-radius: 50% 50% 0 0 / 100% 100% 0 0;
    background: linear-gradient(180deg,
      color-mix(in srgb, var(--accent) 22%, var(--label-bg)),
      var(--label-bg));
  }
  .mandala--bottom-wing {
    left: 0; top: 300px; width: 247px; height: 30px;
    border-radius: 0 0 50% 50% / 0 0 100% 100%;
    background: linear-gradient(0deg,
      color-mix(in srgb, var(--accent) 22%, var(--label-bg)),
      var(--label-bg));
  }
  .mandala--bottom {
    left: 22px; top: 325px; width: 203px; height: 100px;
    border-radius: 8% 8% 50% 50% / 10% 10% 95% 95%;
    background: linear-gradient(0deg,
      color-mix(in srgb, var(--accent) 50%, var(--label-bg)) 0%,
      color-mix(in srgb, var(--accent) 35%, var(--label-bg)) 60%,
      color-mix(in srgb, var(--accent) 15%, var(--label-bg)) 100%);
  }

  .frame-mat {
    position: absolute; left: 33px; top: 160px; width: 181px; height: 170px;
    background: var(--label-bg);
  }
  .frame {
    position: absolute; left: 41px; top: 169px; width: 162px; height: 153px;
    border: 1.5px solid var(--accent);
  }
  .brand {
    position: absolute; left: 79px; top: 185px; width: 81px; height: 23px;
    border: 1px solid var(--gold);
    font-family: "Cinzel", serif; font-size: 14px; color: var(--gold-light);
    text-transform: uppercase; text-align: center; line-height: 21px;
  }
  .lotus {
    position: absolute; left: 92px; top: 218px; width: 61px; height: 84px;
    background: var(--accent);
    clip-path: polygon(50% 0, 64% 10%, 85% 0, 88% 18%, 100% 24%, 94% 50%, 100% 76%, 88% 82%, 85% 100%, 64% 90%, 50% 100%, 36% 90%, 15% 100%, 12% 82%, 0 76%, 6% 50%, 0 24%, 12% 18%, 15% 0, 36% 10%);
  }
  .band {
    position: absolute; left: 0; top: 245px; width: 247px; height: 28px;
    background: #000;
    border-top: 2px solid var(--accent); border-bottom: 2px solid var(--accent);
  }
  .scent {
    position: absolute; left: 0; top: 245px; width: 247px; height: 28px;
    font-family: "Cinzel", serif; font-weight: 700; font-size: 17px;
    text-transform: uppercase; letter-spacing: 0.3px;
    color: var(--accent); text-align: center; line-height: 29px; white-space: nowrap;
  }
  .scent--long { font-size: 13.5px; letter-spacing: 0.4px; }
  .label--lavender .scent { font-size: 16.5px; }
  .dash {
    position: absolute; left: 114px; top: 436px; width: 20px; height: 5px;
    border-radius: 3px; background: var(--accent);
  }
  .claims {
    position: absolute; left: 0; top: 448px; width: 247px;
    list-style: none; text-align: center;
    font-family: "Raleway", sans-serif; font-size: 10.5px; line-height: 13.7px;
    color: var(--accent);
  }
  .claims .origin { font-weight: 700; }
</style>
</head>
<body>
<main class="sheet">
  <section class="label label--dragon">
    <div class="mandala mandala--top" role="img" aria-label="Red line mandala ornament, upper half"></div>
    <div class="mandala mandala--top-wing"></div>
    <div class="mandala mandala--bottom-wing"></div>
    <div class="mandala mandala--bottom" role="img" aria-label="Red line mandala ornament, lower half"></div>
    <div class="frame-mat"></div>
    <div class="frame"></div>
    <div class="brand">Morvel</div>
    <div class="lotus" role="img" aria-label="Red lotus ornament"></div>
    <div class="band"></div>
    <h2 class="scent">Dragon’s Blood</h2>
    <div class="dash"></div>
    <ul class="claims"><li>HAND MADE</li><li>VEGAN FRIENDLY</li><li>NON GMO</li><li>99.99% NATURAL</li><li class="origin">MADE IN THAILAND</li></ul>
  </section>

  <section class="label label--sage">
    <div class="mandala mandala--top" role="img" aria-label="White line mandala ornament, upper half"></div>
    <div class="mandala mandala--top-wing"></div>
    <div class="mandala mandala--bottom-wing"></div>
    <div class="mandala mandala--bottom" role="img" aria-label="White line mandala ornament, lower half"></div>
    <div class="frame-mat"></div>
    <div class="frame"></div>
    <div class="brand">Morvel</div>
    <div class="lotus" role="img" aria-label="White lotus ornament"></div>
    <div class="band"></div>
    <h2 class="scent">White Sage</h2>
    <div class="dash"></div>
    <ul class="claims"><li>HAND MADE</li><li>VEGAN FRIENDLY</li><li>NON GMO</li><li>99.99% NATURAL</li><li class="origin">MADE IN THAILAND</li></ul>
  </section>

  <section class="label label--rain">
    <div class="mandala mandala--top" role="img" aria-label="Green line mandala ornament, upper half"></div>
    <div class="mandala mandala--top-wing"></div>
    <div class="mandala mandala--bottom-wing"></div>
    <div class="mandala mandala--bottom" role="img" aria-label="Green line mandala ornament, lower half"></div>
    <div class="frame-mat"></div>
    <div class="frame"></div>
    <div class="brand">Morvel</div>
    <div class="lotus" role="img" aria-label="Green lotus ornament"></div>
    <div class="band"></div>
    <h2 class="scent">First Rain</h2>
    <div class="dash"></div>
    <ul class="claims"><li>HAND MADE</li><li>VEGAN FRIENDLY</li><li>NON GMO</li><li>99.99% NATURAL</li><li class="origin">MADE IN THAILAND</li></ul>
  </section>

  <section class="label label--lavender">
    <div class="mandala mandala--top" role="img" aria-label="Purple line mandala ornament, upper half"></div>
    <div class="mandala mandala--top-wing"></div>
    <div class="mandala mandala--bottom-wing"></div>
    <div class="mandala mandala--bottom" role="img" aria-label="Purple line mandala ornament, lower half"></div>
    <div class="frame-mat"></div>
    <div class="frame"></div>
    <div class="brand">Morvel</div>
    <div class="lotus" role="img" aria-label="Purple lotus ornament"></div>
    <div class="band"></div>
    <h2 class="scent">Precious Lavender</h2>
    <div class="dash"></div>
    <ul class="claims"><li>HAND MADE</li><li>VEGAN FRIENDLY</li><li>NON GMO</li><li>99.99% NATURAL</li><li class="origin">MADE IN THAILAND</li></ul>
  </section>

  <section class="label label--patch">
    <div class="mandala mandala--top" role="img" aria-label="Cream line mandala ornament, upper half"></div>
    <div class="mandala mandala--top-wing"></div>
    <div class="mandala mandala--bottom-wing"></div>
    <div class="mandala mandala--bottom" role="img" aria-label="Cream line mandala ornament, lower half"></div>
    <div class="frame-mat"></div>
    <div class="frame"></div>
    <div class="brand">Morvel</div>
    <div class="lotus" role="img" aria-label="Cream lotus ornament"></div>
    <div class="band"></div>
    <h2 class="scent">Patchouli</h2>
    <div class="dash"></div>
    <ul class="claims"><li>HAND MADE</li><li>VEGAN FRIENDLY</li><li>NON GMO</li><li>99.99% NATURAL</li><li class="origin">MADE IN THAILAND</li></ul>
  </section>

  <section class="label label--frank">
    <div class="mandala mandala--top" role="img" aria-label="Orange line mandala ornament, upper half"></div>
    <div class="mandala mandala--top-wing"></div>
    <div class="mandala mandala--bottom-wing"></div>
    <div class="mandala mandala--bottom" role="img" aria-label="Orange line mandala ornament, lower half"></div>
    <div class="frame-mat"></div>
    <div class="frame"></div>
    <div class="brand">Morvel</div>
    <div class="lotus" role="img" aria-label="Orange lotus ornament"></div>
    <div class="band"></div>
    <h2 class="scent scent--long">Frankincense &amp; Myrrh</h2>
    <div class="dash"></div>
    <ul class="claims"><li>HAND MADE</li><li>VEGAN FRIENDLY</li><li>NON GMO</li><li>99.99% NATURAL</li><li class="origin">MADE IN THAILAND</li></ul>
  </section>
</main>
</body>
</html>
```